Pediatric Vision Care: Myopia Control Brochure

We are a pediatric eye care practice (ophthalmology and optometry). One of our services we offer for children is myopia control, which are strategies for slowing or stopping the progression of nearsightedness. This is a service we need to sell to parents because most insurance won't pay for it. There are different options we offer that can work well for kids in different situations: glasses with Corvane lenses, atropine eye drops, and/or special contact lenses. We need a brochure we can distribute to parents to let them know about this service that would encourage them to buy it for children who need it. Attached is our initial draft brochure created by our staff that provides text that we want to keep. The images and layout can change. We probably need at least one or two photos of kids on the brochure, because this is only something that works for children who are still growing, and the target audience is parents of 4-8 year old children.

Target Market(s)

Parents of 4-8 year old children

Font styles to use
Sans Serif

Requirements
Must have
• I'm uploading our company logo that should be included somewhere on the brochure. You can include contact information (web address, phone number) for our practice that is found on our website: http://www.brookhollowkidsvision.com/
Should not have
• This should not look childish. We need the impression to be friendly but professional, medical, expert.

```html
<!DOCTYPE html>
<html lang="en">
<head>
<meta charset="utf-8">
<title>Myopia Control Brochure – Brookhollow Kids Vision</title>
<link href="https://fonts.googleapis.com/css2?family=Montserrat:wght@700;800&family=Open+Sans:wght@400;600;700&family=Fira+Sans:wght@500;600;700&display=swap" rel="stylesheet">
<style>
:root{
  --navy:#0d2b6b;
  --blue:#0a66c2;
  --green:#5aa320;
  --orange:#e8640c;
  --ink:#1a1a1a;
  --panel-light:#f3f6f9;
  --white:#ffffff;
}
*{margin:0;padding:0;box-sizing:border-box}
html,body{width:1200px;height:848px;overflow:hidden;background:var(--white)}
body{font-family:"Open Sans",sans-serif;color:var(--ink);position:relative}
.abs{position:absolute}

/* COVER PANEL */
.panel-cover{left:0;top:0;width:350px;height:848px;overflow:hidden;background:var(--white)}
.kid-photo{left:0;top:300px;width:350px;height:460px;
  background:linear-gradient(180deg,#ffffff 0%,#e6efd8 22%,#a9c98a 55%,#6f9a52 80%,#4e7c3a 100%)}
.brand{left:52px;top:62px;display:flex;align-items:center;gap:10px}
.brand-dot{width:26px;height:26px;border-radius:50%;background:var(--blue)}
.brand-name{font-weight:600;font-size:19px;line-height:1.1;color:var(--navy)}
.cover-title{left:36px;top:146px;font-family:"Montserrat",sans-serif;font-weight:800;color:var(--navy);line-height:1}
.cover-title .l1{font-size:50px;display:block;padding-left:2px}
.cover-title .l2{font-size:37px;display:block;margin-top:8px}
.cover-title .l3{font-size:76px;display:block;color:var(--blue);margin-top:2px;letter-spacing:-1px}
.cover-title .l4{font-size:22px;display:block;margin-top:10px;padding-left:3px}
.cover-rule{left:39px;top:353px;width:61px;height:4px;background:var(--navy)}
.cover-intro{left:40px;top:372px;width:240px;font-size:13.5px;line-height:18.5px;letter-spacing:.3px}
.cover-intro b{font-weight:700}
.cover-intro .hl{color:var(--blue);font-weight:700}
.cover-band{left:0;top:690px;width:350px;height:158px}
.cover-tagline{left:90px;top:767px;width:250px;color:var(--white);font-family:"Fira Sans",sans-serif;font-weight:600;font-size:15.5px;line-height:20px;text-align:center}

/* INFO PANEL */
.panel-info{left:350px;top:0;width:332px;height:848px;background:var(--white)}
.icon-badge{width:48px;height:48px;border-radius:50%;display:flex;align-items:center;justify-content:center}
.h-section{font-family:"Fira Sans",sans-serif;font-weight:700;font-size:22px;line-height:21px;color:#111}
.h-rule{height:2px;width:80px}
.body-text{font-size:13px;line-height:16.4px;letter-spacing:-.2px}
.alert-box{left:372px;top:325px;width:283px;height:62px;border:2px solid var(--blue);border-radius:8px;display:flex;align-items:center;gap:14px;padding-left:10px}
.alert-text{font-family:"Montserrat",sans-serif;font-weight:700;font-size:10.5px;line-height:15px;color:var(--navy)}
.how-label{font-size:14px}
.how-sub{font-size:11.5px;letter-spacing:.2px}
.diagram-pill{height:13px;border-radius:7px;color:var(--white);font-family:"Montserrat",sans-serif;font-weight:700;font-size:7px;display:flex;align-items:center;justify-content:center}
.eye-illustration{border-radius:6px;background:radial-gradient(ellipse at 55% 50%,#f08a2c 0%,#e4602a 40%,#f6efe8 72%)}
.diagram-caption{font-size:9px;line-height:12.5px;text-align:center;letter-spacing:.2px}
.info-cta{left:372px;top:772px;font-family:"Fira Sans",sans-serif;font-weight:600;font-size:15.5px;line-height:20px;color:var(--navy)}

/* TREATMENT PANEL */
.panel-treat{left:682px;top:0;width:518px;height:848px;background:var(--panel-light)}
.treat-title{left:682px;top:34px;width:478px;text-align:center;font-family:"Fira Sans",sans-serif;font-weight:700;font-size:22px;color:var(--navy);letter-spacing:.5px}
.treat-sub{left:682px;top:62px;width:478px;text-align:center;font-family:"Fira Sans",sans-serif;font-weight:600;font-size:9.5px;color:var(--green);letter-spacing:.3px}
.treat-row{left:689px;width:496px;display:flex;border-radius:6px;overflow:hidden}
.treat-media{width:206px;flex:none}
.treat-copy{flex:1;padding:4px 6px 0 9px}
.treat-copy h3{font-family:"Fira Sans",sans-serif;font-weight:600;font-size:14.5px;line-height:18px;letter-spacing:.6px;margin-bottom:1px;white-space:nowrap}
.treat-copy p{font-size:11.3px;line-height:11.4px;letter-spacing:.4px}
.treat-copy p+p{margin-top:10px}
.lifestyle-title{left:691px;top:526px;font-family:"Fira Sans",sans-serif;font-weight:700;font-size:17.5px;color:var(--navy);letter-spacing:.6px}
.lifestyle-sub{left:691px;top:548px;width:180px;font-size:10.5px;line-height:13px;color:var(--blue);letter-spacing:.3px}
.life-h{font-family:"Fira Sans",sans-serif;font-weight:600;font-size:12.5px;line-height:13px;letter-spacing:.5px}
.life-text{font-size:8.6px;line-height:12.9px;letter-spacing:.45px}
.dots-v{width:0;border-left:2px dotted #222}
.rule-num{font-family:"Fira Sans",sans-serif;font-weight:600;font-size:20px;color:var(--navy)}
.rule-h{font-family:"Fira Sans",sans-serif;font-weight:600;font-size:17px;line-height:17px;color:var(--navy);letter-spacing:.4px}
.footer-band{left:682px;top:750px;width:518px;height:98px}
.footer-cta{left:757px;top:783px;color:var(--white)}
.footer-cta .big{font-family:"Fira Sans",sans-serif;font-weight:500;font-size:13.5px;line-height:15.5px;letter-spacing:.5px}
.footer-cta .small{font-size:10.5px;margin-top:6px;letter-spacing:.3px}
.contact{left:998px;top:777px;color:var(--white);font-size:10.5px;line-height:14.8px;letter-spacing:.3px}
.contact-line{display:flex;gap:5px;align-items:flex-start}
.contact svg{flex:none;margin-top:2px}
</style>
</head>
<body>

<!-- COVER PANEL -->
<section class="abs panel-cover">
  <div class="abs kid-photo" role="img" aria-label="Smiling boy wearing glasses in a green shirt, sunny park greenery behind"></div>
  <div class="abs brand">
    <span class="brand-dot"></span>
    <span class="brand-name">Brookhollow<br>Kids Vision</span>
  </div>
  <h1 class="abs cover-title">
    <span class="l1">PROTECT</span>
    <span class="l2">YOUR CHILD’S</span>
    <span class="l3">VISION</span>
    <span class="l4">FOR THE FUTURE</span>
  </h1>
  <div class="abs cover-rule"></div>
  <p class="abs cover-intro">Myopia (nearsightedness) is increasing in children -<br><b>but</b> <span class="hl">early treatment<br>can slow it down.</span></p>
  <svg class="abs cover-band" viewBox="0 0 350 158" preserveAspectRatio="none">
    <path d="M0 35 Q170 50 350 0 L350 158 L0 158 Z" fill="#0a66c2"/>
    <path d="M0 45 Q170 58 350 12 L350 158 L0 158 Z" fill="#0d2b6b"/>
  </svg>
  <svg class="abs" style="left:30px;top:760px" width="52" height="58" viewBox="0 0 52 58">
    <path d="M26 2 L49 10 V28 C49 44 38 52 26 56 C14 52 3 44 3 28 V10 Z" fill="#fff"/>
    <path d="M26 8 L43 14 V28 C43 40 35 46 26 50 C17 46 9 40 9 28 V14 Z" fill="#5aa320"/>
    <path d="M26 15 L37 19 V28 C37 36 32 40 26 43 C20 40 15 36 15 28 V19 Z" fill="#3f7f14"/>
  </svg>
  <p class="abs cover-tagline">Early care today can help protect your child’s vision for a lifetime.</p>
</section>

<!-- INFO PANEL -->
<section class="abs panel-info"></section>
<div class="abs icon-badge" style="left:372px;top:47px;background:var(--blue)">
  <svg width="34" height="22" viewBox="0 0 34 22"><path d="M2 11 Q17 -4 32 11 Q17 26 2 11Z" fill="#fff"/><circle cx="17" cy="11" r="6" fill="#0a66c2"/><circle cx="17" cy="11" r="2.5" fill="#fff"/></svg>
</div>
<h2 class="abs h-section" style="left:433px;top:57px">WHAT IS MYOPIA?</h2>
<div class="abs h-rule" style="left:433px;top:87px;background:var(--blue)"></div>
<div class="abs body-text" style="left:375px;top:114px;width:250px">
  <p>Myopia or nearsightedness causes blurry distance vision. Myopia is caused by the elongation of the eVye, and progresses throughout childhood.</p>
  <p style="margin-top:16px">Myopia is becoming increasingly common. More severe myopia and a higher glasses prescription is associated with a higher risk of eye problems involving the retina in adulthood, such as retinal problems and macular degeneration.</p>
</div>
<div class="abs alert-box">
  <svg width="42" height="38" viewBox="0 0 42 38"><path d="M21 2 L40 36 H2 Z" fill="#0d2b6b" stroke="#0d2b6b" stroke-width="3" stroke-linejoin="round"/><rect x="19" y="12" width="4" height="13" rx="2" fill="#fff"/><circle cx="21" cy="30" r="2.4" fill="#fff"/></svg>
  <p class="alert-text">HIGHER MYOPIA TODAY CAN LEAD TO<br>HIGHER RISKS TOMMOROW.</p>
</div>
<div class="abs icon-badge" style="left:371px;top:420px;width:47px;height:47px;background:var(--green)">
  <svg width="30" height="30" viewBox="0 0 30 30"><circle cx="14" cy="16" r="12" fill="none" stroke="#fff" stroke-width="2.5"/><circle cx="14" cy="16" r="7" fill="none" stroke="#fff" stroke-width="2.5"/><circle cx="14" cy="16" r="2.5" fill="#fff"/><path d="M14 16 L26 4 M22 3 L27 3 L27 8" stroke="#fff" stroke-width="2.5" fill="none"/></svg>
</div>
<h2 class="abs h-section" style="left:431px;top:421px">WHAT IS<br>MYOPIA CONTROL?</h2>
<div class="abs h-rule" style="left:431px;top:466px;background:var(--green)"></div>
<p class="abs body-text" style="left:373px;top:486px;width:272px;line-height:15.8px;letter-spacing:-.35px">Myopia control is meant to slow the growthof the eye, keeping the glasses prescription as low as possible and reducing the risk of ocular disease in adulthood.</p>
<p class="abs how-label" style="left:374px;top:557px">How it works:</p>
<p class="abs how-sub" style="left:374px;top:575px">Treatments slow the elongation of the eye</p>
<div class="abs diagram-pill" style="left:391px;top:610px;width:89px;background:var(--navy)">NORMAL EYE</div>
<div class="abs diagram-pill" style="left:512px;top:610px;width:107px;background:var(--green);font-size:6px">MYOPIC (NEARSIGHTED) EYE</div>
<div class="abs eye-illustration" style="left:376px;top:630px;width:118px;height:80px" role="img" aria-label="Cross-section of a normal eye with light focusing on the retina"></div>
<div class="abs eye-illustration" style="left:503px;top:630px;width:122px;height:68px" role="img" aria-label="Cross-section of an elongated myopic eye with light focusing in front of the retina"></div>
<div class="abs" style="left:499px;top:618px;height:120px;border-left:1px dotted #bbb"></div>
<p class="abs diagram-caption" style="left:392px;top:719px;width:80px">Light focuses<br>on the retina</p>
<p class="abs diagram-caption" style="left:500px;top:707px;width:135px">Light focuses<br>in front of the retina,<br>causing blurry distance vision</p>
<p class="abs info-cta">There are several treatment options<br>that can help slow myopia progression.</p>

<!-- TREATMENT PANEL -->
<section class="abs panel-treat"></section>
<h2 class="abs treat-title">TREATMENT OPTIONS</h2>
<p class="abs treat-sub">EACH OPTION HAS BEEN SHOWN TO SLOW MYOPIA PREOGRESSION BY ABOUT 50%</p>

<div class="abs treat-row" style="top:87px;height:134px;background:#f6f5ea">
  <div class="treat-media" role="img" aria-label="Close-up of a spectacle lens with concentric ring optics" style="background:linear-gradient(135deg,#5f9aa0,#2e6f78 60%,#1f5058)"></div>
  <div class="treat-copy">
    <h3 style="color:var(--green);font-size:14px">LUMERIS CORVANE GLASSES LENSES</h3>
    <p>FDA market authorized Lumeris Corvane glasses lenses have been shown to slow myopia progression by about 50% in children aged 6-12.</p>
    <p>These lenses are a great treatment option because all your child needs to do is wear glasses. They look almost identical to ordinary glasses, but use specialized optics to signal the brain to slow the growth of myopic eyes.</p>
  </div>
</div>

<div class="abs treat-row" style="top:225px;height:144px;background:#fbf3e8">
  <div class="treat-media" role="img" aria-label="Soft contact lens balanced on a fingertip" style="background:radial-gradient(ellipse at 55% 60%,#4aa3c8 0%,#1c5f80 18%,#b8603e 34%,#3a1a12 62%,#0a0a0a 90%)"></div>
  <div class="treat-copy">
    <h3 style="color:var(--orange)">LOW-DOSE ATROPINE</h3>
    <p>These eyedrops have been studied for over 20 years and have been shown to slow myopia progression by about 50% when used consistently.</p>
    <p style="margin-top:11px">Low-dose atropine is simple to add to your daily routine. One drop is placed in each eye before bed each evening. These are ordered from a compounding pharmacy and mailed directly to your home.</p>
  </div>
</div>

<div class="abs treat-row" style="top:372px;height:144px;background:#eef3f9">
  <div class="treat-media" role="img" aria-label="Eye-drop bottle tip releasing a single drop" style="background:linear-gradient(120deg,#dfe4e8 0%,#8a97a2 30%,#4c5965 65%,#2e3944)"></div>
  <div class="treat-copy">
    <h3 style="color:var(--blue)">SPECIALTY CONTACT LENSES</h3>
    <p style="line-height:12.6px">FDA-approved ClearPath lenses have been shown to slow myopia progression by about 50% in children aged 8-12.</p>
    <p style="line-height:12.6px">Contact lenses can be a great fit for many children, especially active children or those who do not enjoy wearing glasses.<br>Many children as young as 7 or 8 are successful at wearing contacts.</p>
  </div>
</div>

<h2 class="abs lifestyle-title">LIFESTYLE OPTIONS</h2>
<p class="abs lifestyle-sub">All myopic children can benefit from these lifestyle changes.</p>
<h3 class="abs life-h" style="left:691px;top:577px;color:var(--green)">GET OUTDOORS<br>EVERYDAY</h3>
<p class="abs life-text" style="left:689px;top:605px;width:148px">There is strong evidence that children who spend at least 2 hours a day outdoors are less likely to become myopic, and their myopia progresses slower than children who are outdoors less. Some studies show that increasing outdoor time by as few as 45 minutes a day is beneficial in reducing progression.</p>
<div class="abs dots-v" style="left:853px;top:590px;height:162px"></div>
<svg class="abs" style="left:906px;top:545px" width="48" height="38" viewBox="0 0 48 38"><rect x="2" y="2" width="44" height="26" rx="2" fill="none" stroke="#e8640c" stroke-width="3.5"/><rect x="21" y="28" width="6" height="5" fill="#e8640c"/><rect x="13" y="33" width="22" height="3" fill="#e8640c"/></svg>
<h3 class="abs life-h" style="left:876px;top:585px;color:var(--orange);line-height:15px">LIMIT SCREEN TIME<br>AND NEAR WORK</h3>
<p class="abs life-text" style="left:875px;top:620px;width:138px">There is some evidence that consistent use of screens, particularly held very close to the face, can worsen nearsightedness.<br>We recommend limiting nonacademic screen time and near work.</p>
<div class="abs dots-v" style="left:1029px;top:540px;height:202px"></div>
<p class="abs rule-num" style="left:1052px;top:538px">20 -20 -20</p>
<svg class="abs" style="left:1075px;top:564px" width="34" height="22" viewBox="0 0 34 22"><path d="M2 11 Q17 -4 32 11 Q17 26 2 11Z" fill="#0d2b6b"/><path d="M7 11 Q17 2 27 11 Q17 20 7 11Z" fill="#f3f6f9"/><circle cx="17" cy="11" r="4.5" fill="#0d2b6b"/></svg>
<h3 class="abs rule-h" style="left:1048px;top:601px">Use the<br>20-20-20 Rule</h3>
<p class="abs life-text" style="left:1048px;top:638px;width:130px">Every 20 minutes take a 20 second break to look at least 20 feet away.</p>

<svg class="abs footer-band" viewBox="0 0 518 98" preserveAspectRatio="none">
  <path d="M0 16 Q260 -6 518 14 L518 98 L0 98 Z" fill="#0d2b6b"/>
</svg>
<svg class="abs" style="left:710px;top:783px" width="42" height="46" viewBox="0 0 42 46">
  <rect x="2" y="6" width="38" height="38" rx="3" fill="none" stroke="#fff" stroke-width="3"/>
  <rect x="2" y="6" width="38" height="8" fill="#fff"/>
  <rect x="10" y="1" width="3" height="9" fill="#fff"/><rect x="29" y="1" width="3" height="9" fill="#fff"/>
  <g fill="#fff"><rect x="8" y="19" width="6" height="5"/><rect x="18" y="19" width="6" height="5"/><rect x="28" y="19" width="6" height="5"/><rect x="8" y="27" width="6" height="5"/><rect x="18" y="27" width="6" height="5"/><rect x="28" y="27" width="6" height="5"/><rect x="8" y="35" width="6" height="5"/><rect x="18" y="35" width="6" height="5"/></g>
</svg>
<div class="abs footer-cta">
  <p class="big">START PROTECTING<br>YOUR CHILD’S VISION TODAY!</p>
  <p class="small">Schedule a myopia control consultation.</p>
</div>
<div class="abs dots-v" style="left:985px;top:778px;height:62px;border-color:#fff"></div>
<div class="abs contact">
  <p class="contact-line"><svg width="10" height="10" viewBox="0 0 10 10"><circle cx="5" cy="5" r="4.2" fill="none" stroke="#fff"/><ellipse cx="5" cy="5" rx="1.8" ry="4.2" fill="none" stroke="#fff"/><path d="M1 5H9" stroke="#fff"/></svg>brookhollowkidsvision.com</p>
  <p class="contact-line"><svg width="10" height="10" viewBox="0 0 10 10"><path d="M2 1 L4 1 L5 3.5 L3.8 4.5 Q5 6.5 6 6.3 L7 5 L9.5 6 L9.5 8 Q9 9.5 7.5 9.5 Q1 8 0.5 2.5 Q0.5 1 2 1Z" fill="#fff"/></svg>(555) 014 - 2020</p>
  <p class="contact-line"><svg width="10" height="13" viewBox="0 0 10 13"><path d="M5 12 Q1 7 1 4.5 A4 4 0 0 1 9 4.5 Q9 7 5 12Z" fill="none" stroke="#fff" stroke-width="1.3"/><circle cx="5" cy="4.5" r="1.4" fill="#fff"/></svg>4100 Alder Crest Way, Suite 120<br>Fairbrook, VA 22190</p>
</div>

</body>
</html>
```